Label Sticker for Tea Bag and Herbs and Spices Bag

I want to design the product label sticker size in 60 mm (H) x 100 mm (W).
This label is for our product herbal tea bag. We sell herbs such as Rose buds, Lavender, Chamomile, etc they are consider flower tea. Our products are natural dry herbs and spices.
I select Green, Brown, white as color combination. I can accept other colour proposed. If it look nice. However, only maximum 3 colours to play around and white is a compulsory colour.
I will print the product name, description, expiry date and instruction how to use and company name and address on it in black ink.
Prefer the label have natural look.
I would like to place my company logo in the label. Attached is the full colour artwork logo file.
I can accept one colour for logo since I only use 3 maximum colour.

Please advise the best design.

Reason: I am sorry as first time use Tally orchard, I am not sure how to use the system.

Target Market(s)

To consumer who drink tea

Industry/Entity Type

It Company

Font styles to use
Serif

Requirements
Must have
• 60 mm (H) x 100 mm (w)
• Maximum 3 colour to play.
• Natural look and attraction to consumers.
Nice to have
• -Some drawing such as flower or leaves, lines, waves... as wallpaper
• -Can use 3 colour to separate Products name, Description and How to use.
• -Can give different colour besides my request for comparison.
• -Nice frame
Should not have
• Big pictures - Because it take the spaces, I cannot write more information in the label
• Too dark colour -Consumer cannot see the product information very clearly
• Too big logo - As it will take the space of the label.

```html
<!DOCTYPE html>
<html lang="en">
<head>
<meta charset="utf-8">
<title>Herbal Tea Label</title>
<link rel="stylesheet" href="https://fonts.googleapis.com/css2?family=Cinzel:wght@400;500&family=Tinos&family=Lora:ital@1&display=swap">
<style>
  :root {
    --stripe-light: #c9986c;
    --stripe-dark: #9c6a45;
    --card: #ffffff;
    --card-edge: #b9dc8c;
    --leaf: #7cb52f;
    --leaf-soft: #b6dc7d;
    --brand: #d97a1f;
    --title: #8a3a1c;
    --rule: #8a4a28;
    --rule-faint: #e3d3c4;
    --ink: #111111;
  }
  * { box-sizing: border-box; margin: 0; padding: 0; }
  html, body { width: 717px; height: 1200px; overflow: hidden; }
  body {
    position: relative;
    background: repeating-linear-gradient(0deg,
      var(--stripe-light) 0 30px,
      var(--stripe-dark) 30px 60px);
  }
  /* 100 mm x 60 mm sticker, set sideways on the tall sheet */
  .label {
    position: absolute;
    left: -191.5px; top: 270px;
    width: 1100px; height: 660px;
    transform: rotate(-90deg);
    background: var(--card);
    border: 5px solid var(--card-edge);
    border-radius: 52px;
  }
  .flourish {
    position: absolute;
    width: 140px; height: 140px;
    background: radial-gradient(circle at var(--fx) var(--fy), var(--leaf) 0%, var(--leaf-soft) 35%, rgba(182,220,125,0) 68%);
  }
  .flourish--tl { left: 28px;  top: 24px;    --fx: 18%; --fy: 18%; }
  .flourish--tr { right: 28px; top: 24px;    --fx: 82%; --fy: 18%; }
  .flourish--bl { left: 28px;  bottom: 24px; --fx: 18%; --fy: 82%; }
  .flourish--br { right: 28px; bottom: 24px; --fx: 82%; --fy: 82%; }
  .brand {
    position: absolute;
    left: 0; right: 0; top: 36px;
    text-align: center;
    font-family: "Cinzel", serif;
    font-weight: 500;
    font-size: 32px;
    letter-spacing: 1px;
    color: var(--brand);
  }
  .product-name {
    position: absolute;
    left: 0; right: 0; top: 92px;
    text-align: center;
    font-family: "Cinzel", serif;
    font-weight: 400;
    font-size: 60px;
    line-height: 1.2;
    color: var(--title);
  }
  .title-rules {
    position: absolute;
    left: 180px; top: 178px;
    width: 730px; height: 16px;
  }
  .details {
    position: absolute;
    left: 60px; top: 222px;
    width: 560px;
    text-align: center;
  }
  .category {
    font-family: "Tinos", serif;
    font-weight: 700;
    font-size: 32px;
    color: var(--ink);
  }
  .description {
    margin: 26px 20px 0;
    font-family: "Tinos", serif;
    font-size: 22px;
    line-height: 1.35;
    color: var(--ink);
  }
  .tagline {
    margin-top: 40px;
    font-family: "Lora", serif;
    font-style: italic;
    font-size: 28px;
    color: var(--title);
  }
  .print-area {
    position: absolute;
    left: 650px; top: 230px;
    width: 370px; height: 300px;
    border-left: 2px solid var(--rule);
    background: repeating-linear-gradient(180deg,
      transparent 0 48px,
      var(--rule-faint) 48px 50px);
    background-clip: content-box;
    padding-left: 24px;
  }
  .net-weight {
    position: absolute;
    left: 0; right: 0; top: 580px;
    text-align: center;
    font-family: "Tinos", serif;
    font-size: 22px;
    color: var(--ink);
  }
</style>
</head>
<body>
  <main class="label">
    <div class="flourish flourish--tl" role="img" aria-label="Green scrolling leaf flourish, top left corner"></div>
    <div class="flourish flourish--tr" role="img" aria-label="Green scrolling leaf flourish, top right corner"></div>

    <p class="brand">Verdant Leaf</p>

    <h1 class="product-name">Product's Name</h1>
    <svg class="title-rules" viewBox="0 0 730 16" aria-hidden="true">
      <rect x="0" y="0" width="730" height="6" fill="var(--rule)"/>
      <rect x="0" y="11" width="730" height="3" fill="var(--rule)"/>
    </svg>

    <section class="details">
      <h2 class="category">Herbal Tea</h2>
      <p class="description">A floral infusion of “White tea (Camella Sinensis), Blueberries, Elderberries, Cornflowers and Scotch Heather”.</p>
      <p class="tagline">Ancient Remedies for Modern Life</p>
    </section>

    <div class="print-area" aria-label="Space for expiry date, instructions and company address"></div>

    <p class="net-weight">NET WT. 15g / 0.5 oz</p>

    <div class="flourish flourish--bl" role="img" aria-label="Green scrolling leaf flourish, bottom left corner"></div>
    <div class="flourish flourish--br" role="img" aria-label="Green scrolling leaf flourish, bottom right corner"></div>
  </main>
</body>
</html>
```